Center for Cellular Datawork wordpress design

We need a wordpress design for the new Center for Cellular Datawork at the Marrowfield University. We are a research institute focused on medical and biological research involving big data and informatics. The website has to be eyecatching and appropriate for an academic context, with easily updated content.

Press release here: http://www.mfhs.marrowfield-u.edu/news/News_Releases/2013/02/cellular/

We would prefer to use images from our research labs over stock art, but feel free to use placeholders for now. Please contact me if there are specific types of images you need.

Target Market(s)

Tech-savvy academics, faculty, students, general laypeople

Industry/Entity Type

Medical

Requirements
Must have
• Use existing logo (attached, other versions available upon request)

Sections for:
Mission statement (draft version attached)
Educational Programs: there is only one at the moment, but we will need the option to add more
Faculty members/resident staff (contact database); webform to apply to join
Events calendar/list
Emphasis on search engine optimization
Nice to have
• News/publication tabs for the front page (similar to those on http://www.ovrek.marrowfield-u.edu/)

It would be helpful if you could use the Marrowfield color palette: http://www.marrowfield-u.edu/webservices/styleguide/color.html

```html
<!DOCTYPE html>
<html lang="en">
<head>
<meta charset="utf-8">
<title>Center for Cellular Datawork</title>
<link href="https://fonts.googleapis.com/css2?family=Arimo:wght@400;700&family=Noto+Serif:wght@400;700&display=swap" rel="stylesheet">
<style>
:root{
  --navy:#1f2d6b;
  --navy-dark:#18245a;
  --red:#a8232a;
  --red-dark:#8e1c22;
  --text:#555;
  --muted:#888;
  --line:#dcdcdc;
  --panel:#e6e2dd;
  --panel-dark:#d4cfc8;
  --page:#ebebeb;
  --white:#fff;
}
*{box-sizing:border-box;margin:0;padding:0}
html,body{width:1022px;height:1200px;overflow:hidden}
body{position:relative;background:var(--page);font-family:"Arimo",Arial,sans-serif;color:var(--text);font-size:12px}
.abs{position:absolute}
a{color:inherit;text-decoration:none}
.serif{font-family:"Noto Serif",Georgia,serif}

/* header */
.site-header{left:0;top:0;width:1022px;height:113px;background:linear-gradient(#f4f4f4,#e9e9e9)}
.brand{left:76px;top:30px;display:flex;align-items:center;gap:10px}
.brand-mark{width:34px;height:34px;border-radius:50%;background:var(--navy)}
.brand-name{font-size:24px;line-height:26px;color:var(--navy);width:260px}
.top-links{left:677px;top:24px;font-size:10px;color:var(--red)}
.top-links span{color:var(--muted);margin:0 8px}
.search{left:802px;top:17px;width:144px;height:24px;background:var(--white);border:1px solid #d3d3d3;font-size:10px;color:#999;padding:6px 10px}
.search svg{position:absolute;right:7px;top:5px}

/* nav */
.main-nav{left:0;top:113px;width:1022px;height:43px;background:linear-gradient(#34438a,#1e2b68);border-top:2px solid #16205a}
.main-nav ul{position:absolute;left:76px;top:0;display:flex;list-style:none;height:41px}
.main-nav li{color:var(--white);font-size:12.5px;line-height:41px;padding:0 20px;border-right:1px solid #142058;border-left:1px solid #4453a0;font-family:"Noto Serif",Georgia,serif}
.main-nav li.current{background:linear-gradient(#b02a30,#8e1c22)}

.breadcrumb{left:100px;top:168px;font-size:10px;color:var(--red)}
.breadcrumb b{font-weight:400;color:var(--navy);margin-left:6px}
.breadcrumb i{font-style:normal;color:var(--navy);margin:0 6px 0 8px}

/* main */
.main-box{left:76px;top:190px;width:871px;height:921px;background:var(--white);border:1px solid #e0e0e0}
.slider{left:84px;top:197px;width:854px;height:293px;border:2px solid #e2e4ef;background:linear-gradient(100deg,#9bb0de 0%,#d9dff0 35%,#f0eef3 60%,#e8e6f0 100%)}
.slider-shadow{left:76px;top:492px;width:871px;height:18px;background:radial-gradient(ellipse at top,rgba(0,0,0,.18),transparent 70%)}
.caption{left:94px;top:428px;width:576px;height:43px;background:rgba(90,90,90,.82);color:var(--white);font-size:16px;padding:10px 22px}
.caption .go{position:absolute;right:10px;top:8px;width:28px;height:28px;border-radius:50%;background:var(--white)}
.edu{left:683px;top:219px;width:236px;height:251px;background:linear-gradient(#6b6b6b,#2e2e2e);border:1px solid #888;color:#eee}
.edu h3{height:43px;background:#6c6c6c;border-bottom:1px solid #444;font-size:14.5px;padding:12px 17px;letter-spacing:.5px;font-weight:400}
.edu .thumb{position:absolute;left:10px;top:54px;width:95px;height:70px;background:linear-gradient(135deg,#6f6a5a,#b9b6a9 50%,#4d5a3f);border:2px solid #222}
.edu .lede{position:absolute;left:114px;top:54px;width:114px;font-size:11px;line-height:16px}
.edu .date{position:absolute;left:114px;top:108px;font-size:11px;color:#bbb}
.edu .body{position:absolute;left:12px;top:134px;width:214px;font-size:11px;line-height:18px;text-align:justify}
.edu .all{position:absolute;left:0;bottom:0;width:100%;height:34px;border-top:1px solid #222;font-size:12px;padding:9px 14px}

h2.section{font-size:16.5px;color:var(--red);letter-spacing:.5px;font-weight:400}
.welcome-title{left:86px;top:535px}
.welcome-text{left:86px;top:571px;width:408px;font-size:12px;line-height:19.6px;text-align:justify;hyphens:auto;-webkit-hyphens:auto}
.welcome-photo{left:511px;top:576px;width:158px;height:142px;border:5px solid #eee;background:linear-gradient(160deg,#d5e4f3,#6f9cc6 55%,#c3d8ec)}
.rule{left:86px;width:584px;height:1px;background:var(--line)}
.tabs{left:86px;top:768px;font-size:14.5px;font-family:"Noto Serif",Georgia,serif}
.tabs .active{color:var(--red);border-bottom:3px solid var(--red);padding-bottom:4px;display:inline-block}
.tabs .sep{color:#999;margin:0 20px}
.tabs .inactive{color:#999}
.tab-arrow{left:132px;top:794px}
.circle-btn{width:16px;height:16px;border-radius:50%;background:#999}
.news-photo{left:87px;width:248px;height:124px;border:6px solid #eee}
.news-text{left:349px;width:321px;font-size:12.4px;line-height:19.6px;text-align:justify}
.more{left:349px;font-size:13px;color:var(--navy)}

/* sidebar */
.events{left:695px;top:538px;width:243px;height:299px;background:linear-gradient(#f2f0ed,var(--panel-dark));border:1px solid #d0ccc6}
.events h3,.faculty h3{font-size:14px;color:var(--red);font-weight:400;padding:13px 14px;letter-spacing:.3px}
.events h3{border-bottom:1px solid #d6d2cc;margin:0 10px;padding-left:4px}
.event{position:absolute;left:10px;width:225px}
.event .pic{position:absolute;left:0;top:0;width:66px;height:66px;border:3px solid #dcd8d2}
.event p{position:absolute;left:77px;top:0;width:148px;font-size:11px;line-height:16px}
.event .d{position:absolute;left:77px;top:55px;font-size:11px;color:var(--navy)}
.faculty{left:695px;top:842px;width:243px;height:246px;background:linear-gradient(#f2f0ed,var(--panel-dark));border:1px solid #d0ccc6}
.faces{position:absolute;left:11px;top:53px;display:grid;grid-template-columns:repeat(4,46px);gap:11px 11px}
.faces div{width:46px;height:46px;border:2px solid var(--white)}
.faculty .divider{position:absolute;left:10px;top:172px;width:222px;height:1px;background:#c9c4bd}
.btn{position:absolute;top:188px;width:112px;height:26px;background:linear-gradient(#a9adb3,#767b82);border:1px solid #666;color:var(--white);font-size:11px;text-align:center;line-height:24px;font-family:"Noto Serif",Georgia,serif;white-space:nowrap}
.btn.login{left:6px}
.btn.register{left:123px}

/* footer */
.footer-links{left:0;top:1129px;width:1022px;text-align:center;font-size:11px;color:#666}
.footer-links span{color:#999;margin:0 7px}
.copyright{left:76px;top:1162px;font-size:11px;color:#666}
.social{left:900px;top:1158px;display:flex;gap:6px}
.social div{width:21px;height:21px;border-radius:3px}
</style>
</head>
<body>

<header class="site-header abs">
  <div class="brand abs"><div class="brand-mark"></div><div class="brand-name">Center for Cellular Datawork</div></div>
  <nav class="top-links abs"><a>HOME</a><span>|</span><a>ABOUT US</a></nav>
  <div class="search abs">Search
    <svg width="14" height="14" viewBox="0 0 14 14"><circle cx="5.5" cy="5.5" r="4" fill="none" stroke="#333" stroke-width="2"/><line x1="8.5" y1="8.5" x2="13" y2="13" stroke="#333" stroke-width="2.5"/></svg>
  </div>
</header>

<nav class="main-nav abs">
  <ul>
    <li class="current">COURSES AND PROGRAMS</li><li>LATEST NEWS</li><li>LATEST EVENTS</li><li>MEMBERS</li><li>LINKS</li><li>CONTACT US</li><li>HELP</li>
  </ul>
</nav>

<div class="breadcrumb abs">HOME<i>››</i><b>Welcome</b></div>

<main>
  <div class="main-box abs"></div>
  <div class="slider abs" role="img" aria-label="Lab researcher in mask and blue gloves filling a flask with a pipette"></div>
  <div class="slider-shadow abs"></div>
  <div class="caption abs serif">Quisque urna lacus, consequat sed malesuada ac, tristique.
    <span class="go"><svg width="28" height="28" viewBox="0 0 28 28"><path d="M12 9l5 5-5 5" fill="none" stroke="#333" stroke-width="2.5"/></svg></span>
  </div>

  <section class="edu abs">
    <h3 class="serif">EDUCATIONAL PROGRAMS</h3>
    <div class="thumb" role="img" aria-label="Researchers working in a laboratory"></div>
    <p class="lede">Donec gravida cond imentum duit eget con sequat arcu elit.</p>
    <p class="date">Mar-13-2013</p>
    <p class="body">Sed ac aliquet justo. Praesent id augue elit. Morbi pulvinar orci vel est fringilla pharetra in a ipsum. Vestibulum sceleris-que, odio sed bibendum.</p>
    <div class="all serif">▸&nbsp; VIEW ALL</div>
  </section>

  <h2 class="section welcome-title abs serif">WELCOME TO OUR SITE</h2>
  <p class="welcome-text abs">The goal of the CCD is to become a national leader in biomedical informatics, spanning the disciplines of bioinformatics at the molecular level, to medical informatics for patients and populations. The institute will support interdisciplinary research and education in biomedical informatics at the Marrowfield University. Interdisciplinary studies are impeded not by any single barrier, but rather an array of tiny hurdles. The CCD will aid faculty, trainees, and staff in clearing these hurdles, thus elevating biomedical informatics research throughout the greater Marrowfield community.</p>
  <div class="welcome-photo abs" role="img" aria-label="Blue DNA double helix render"></div>

  <div class="rule abs" style="top:748px"></div>
  <div class="tabs abs"><span class="active">LATEST NEWS</span><span class="sep">|</span><span class="inactive">PUBLICATION</span></div>
  <div class="rule abs" style="top:794px;left:196px;width:474px"></div>
  <svg class="tab-arrow abs" width="16" height="9" viewBox="0 0 16 9"><path d="M0 0h16L8 9z" fill="#a8232a"/></svg>
  <div class="circle-btn abs" style="left:651px;top:768px"><svg width="16" height="16" viewBox="0 0 16 16"><path d="M7 4.5l3.5 3.5L7 11.5" fill="none" stroke="#fff" stroke-width="2"/></svg></div>

  <div class="news-photo abs" style="top:822px;background:linear-gradient(120deg,#8fa3c8,#dfe6f1 45%,#c9d4e6)" role="img" aria-label="Gloved hand using a pipette over a test tube"></div>
  <p class="news-text abs" style="top:823px">Curabitur ac massa et erat mattis aliquam. Pellentesque tempor viverra metus non vehicula. Sed auctor ligula quis odio elementum ac ultricies massa faucibus. Pellentesque sit amet urna elit, ornare sollicitudin nisi. Nunc aliquam placerat tortor, ac fermentum urna tristique at.</p>
  <div class="more abs serif" style="top:928px">VIEW MORE</div>

  <div class="news-photo abs" style="top:965px;background:linear-gradient(100deg,#c9a66b,#e9d9a8 45%,#c7d27a)" role="img" aria-label="Scientist in safety goggles examining a sample tube"></div>
  <p class="news-text abs" style="top:966px">Curabitur ac massa et erat mattis aliquam. Pellentesque tempor viverra metus non vehicula. Sed auctor ligula quis odio elementum ac ultricies massa faucibus. Pellentesque sit amet urna elit, ornare sollicitudin nisi. Nunc aliquam placerat tortor, ac fermentum urna tristique at.</p>
  <div class="more abs serif" style="top:1071px">VIEW MORE</div>
</main>

<aside>
  <section class="events abs">
    <h3 class="serif">LATEST EVENTS</h3>
    <div class="circle-btn abs" style="left:212px;top:14px"><svg width="16" height="16" viewBox="0 0 16 16"><path d="M7 4.5l3.5 3.5L7 11.5" fill="none" stroke="#fff" stroke-width="2"/></svg></div>
    <div class="event" style="top:53px"><div class="pic" style="background:linear-gradient(135deg,#0d2f5a,#49b6e6 50%,#d8eef8)" role="img" aria-label="Row of blue sample vials"></div><p>Sed commodo, sem a pellen mollis enim, ac pulvinar odio elit in tincidunt.</p><span class="d">Mar-03-2013</span></div>
    <div class="event" style="top:134px"><div class="pic" style="background:linear-gradient(135deg,#2c3d6a,#8a9dbb 55%,#5c4b3a)" role="img" aria-label="Researchers in discussion"></div><p>Sed commodo, sem a pellen mollis enim, ac pulvinar odio elit in tincidunt.</p><span class="d">Mar-03-2013</span></div>
    <div class="event" style="top:215px"><div class="pic" style="background:radial-gradient(circle,#6ec6f2,#13539a 60%,#061c3c)" role="img" aria-label="Blue render of a human brain"></div><p>Sed commodo, sem a pellen mollis enim, ac pulvinar odio elit in tincidunt.</p><span class="d">Mar-03-2013</span></div>
  </section>

  <section class="faculty abs">
    <h3 class="serif">FACULTY MEMBERS &amp; STAFFS</h3>
    <div class="faces">
      <div style="background:#8a6a58" role="img" aria-label="Faculty member portrait"></div>
      <div style="background:#7d8f5c" role="img" aria-label="Faculty member portrait"></div>
      <div style="background:#e9e4ea" role="img" aria-label="Staff avatar"></div>
      <div style="background:#dfe8b8" role="img" aria-label="Staff avatar"></div>
      <div style="background:#a59a8a" role="img" aria-label="Faculty member portrait"></div>
      <div style="background:#f1f1f1" role="img" aria-label="Staff avatar"></div>
      <div style="background:#8a8a8a" role="img" aria-label="Faculty member portrait"></div>
      <div style="background:#b9a8c6" role="img" aria-label="Staff avatar"></div>
    </div>
    <div class="divider"></div>
    <div class="btn login">MEMBER LOGIN</div>
    <div class="btn register">REGISTER NOW</div>
  </section>
</aside>

<footer>
  <nav class="footer-links abs">Home<span>|</span>About us<span>|</span>Courses and Programs<span>|</span>Latest News<span>|</span>Latest Events<span>|</span>Members<span>|</span>Links<span>|</span>Contact us<span>|</span>Help<span>|</span>Register<span>|</span>Member Login</nav>
  <p class="copyright abs">Copyright &nbsp;©&nbsp; 2013 &nbsp; www.cellulardatawork.org &nbsp; All rights reserved.</p>
  <div class="social abs"><div style="background:#3b5a9a"></div><div style="background:#3fa9dd"></div></div>
</footer>

</body>
</html>
```